依頼詳細
スナックビルのテナント様募集(オーナーママ募集)のチラシデザインをお願いします。

新聞折り込み、ポスティングで配布しようと考えていますのでターゲットの女性の目に留まるような女性的なデザイン制作をお願いします。

オーナーママが未経験の方でも、お店をしてみたいと思いお問い合わせに繋がるようにお願いします。
記載項目
社名:株式会社 楓/電話番号:0120-3-71928/URL:http://kaede-hanamaru.co.jp/

ビル名:メゾン楓ビル31北浜Ⅲ、ビル所在地:大阪市西成区玉出3丁目8-21

各部屋:賃料、共益費、礼金、面積、席数

各部屋写真:添付します。一枚添付しますが、3部屋掲載お願いします。※同じ写真でお願いします。

地図

以前作ったチラシを添付しますので、そのチラシ下部に記載してある会社名から宅建番号など
は記載お願いします。※デザインは変わってもOKです。
サイズ
A4
ページ数
片面
希望イメージ
シンプル 複雑
単色 カラフル
暗い 明るい
日常 高級
遊び心 厳粛
未来的 伝統的
女性的 男性的
希望する色
ピンクor水色
納品ファイル
• 高解像度JPG (.jpg)
• イラストレーター形式 (.ai)
補足説明
以前作ったチラシを添付します。

賃料、共益費、礼金、面積、席数の数字は適当な金額でお願いします。

地図の部分は空白でお願いします。
必ずコンペの当選者を選定する欄にチェックを入れ忘れていました。
多数のご提案、本当にありがとうございます。

どの提案も素晴らしいもので、決めかねております。

月曜日までに決定したいと思いますので、延長させていただきました。

よろしくお願いします。

・直感的にやわらかくイメージできる、イラストを使っていて好感が持てる。
・どうしても夜のイメージが強い業種なのに、さわやかに表現している。
・アイデア・発想がすばらしい。

この度は多数のご提案ありがとうございました。今回、1名様のご提案を採用させて頂きました。残念ながら採用されなかった方々のご提案も完成度が高く、決定までに時間を要してしまい大変申し訳ございませんでした。また次回の依頼で、皆様にご協力頂けますと幸いです。どうぞ、よろしくお願い致します。

```html
<!DOCTYPE html>
<html lang="ja">
<head>
<meta charset="utf-8">
<title>テナント様募集中 メゾン楓ビル31北浜Ⅲ</title>
<link href="https://fonts.googleapis.com/css2?family=Noto+Sans+JP:wght@400;700;900&family=M+PLUS+Rounded+1c:wght@500;800&display=swap" rel="stylesheet">
<style>
:root{
  --rose:#e8417a;
  --rose-deep:#d6195a;
  --magenta:#c4127a;
  --blush:#fbe0ea;
  --petal:#f6bfd3;
  --cream:#fff6f8;
  --wine:#8c1d3a;
  --ink:#4a2a33;
  --amber-dark:#3a1c10;
  --amber:#a4552a;
  --white:#ffffff;
}
*{margin:0;padding:0;box-sizing:border-box}
html,body{width:849px;height:1200px;overflow:hidden;background:var(--white)}
body{font-family:"Noto Sans JP",sans-serif;color:var(--ink)}
.flyer{position:relative;width:849px;height:1200px;overflow:hidden;background:var(--cream)}
.rose-backdrop{position:absolute;inset:0 0 110px 0;
  background:
    radial-gradient(circle at 12% 8%,var(--petal) 0,transparent 22%),
    radial-gradient(circle at 90% 45%,var(--petal) 0,transparent 25%),
    radial-gradient(circle at 8% 70%,var(--petal) 0,transparent 22%),
    radial-gradient(circle at 70% 95%,var(--petal) 0,transparent 20%),
    linear-gradient(180deg,var(--blush),#fff0f4 60%,var(--blush));}
.abs{position:absolute}
.headline{left:0;top:12px;width:760px;text-align:center;font-family:"M PLUS Rounded 1c",sans-serif;font-weight:800;font-size:64px;letter-spacing:2px;color:var(--rose-deep);
  text-shadow:3px 0 0 #fff,-3px 0 0 #fff,0 3px 0 #fff,0 -3px 0 #fff,2px 2px 0 #fff,-2px -2px 0 #fff,2px -2px 0 #fff,-2px 2px 0 #fff,0 4px 8px rgba(140,29,58,.35)}
.building-name{left:120px;top:94px;font-weight:900;font-size:34px;color:var(--magenta);text-shadow:2px 2px 0 #fff,-2px -2px 0 #fff,2px -2px 0 #fff,-2px 2px 0 #fff}
.building-name .num{font-size:40px}
.address{left:120px;top:140px;font-size:15px;font-weight:700;color:var(--ink)}
.map-slot{left:518px;top:108px;width:232px;height:160px;background:var(--white);border:2px solid #ddd;display:flex;align-items:center;justify-content:center;font-size:36px;font-weight:700;color:#222}
.building-photo{left:752px;top:86px;width:97px;height:254px;background:linear-gradient(180deg,#2c1b2e,#6b3a4a 55%,#c06a4a)}
.recruit-tag{left:28px;top:190px;width:228px;height:38px;border-radius:19px;background:var(--rose);color:#fff;font-weight:900;font-size:24px;text-align:center;line-height:38px;letter-spacing:2px}
.lead{left:30px;top:238px;width:470px;font-family:"M PLUS Rounded 1c",sans-serif;font-weight:800;font-size:19px;line-height:1.5;color:var(--rose-deep)}
.welcome-band{left:-20px;top:324px;width:780px;height:40px;border-radius:20px;background:linear-gradient(90deg,var(--rose),#f07aa0);color:#fff;font-weight:900;font-size:24px;line-height:40px;text-align:center;letter-spacing:1px}
.welcome-band .accent{color:#ffe46b}
.room-photo{width:382px;height:184px;background:linear-gradient(135deg,var(--amber-dark),var(--amber) 50%,#e3a66a 80%,var(--amber-dark));border:4px solid #fff;box-shadow:0 3px 8px rgba(0,0,0,.25)}
.photo-a{left:184px;top:382px}
.photo-b{left:283px;top:596px}
.photo-c{left:57px;top:800px}
.spec{width:236px;background:rgba(255,255,255,.85);padding:6px 12px;border-radius:6px;font-size:19px;font-weight:700;color:var(--rose-deep)}
.spec div{display:flex;justify-content:space-between;border-bottom:1px dotted var(--rose);padding:3px 0}
.spec div:last-child{border-bottom:none}
.spec dt{letter-spacing:4px;color:var(--wine)}
.spec-a{left:584px;top:400px}
.spec-b{left:40px;top:618px}
.spec-c{left:474px;top:816px}
.support-note{left:14px;top:418px;width:160px;font-family:"M PLUS Rounded 1c",sans-serif;font-weight:800;font-size:17px;line-height:1.55;color:var(--rose-deep);text-shadow:0 0 4px #fff}
.fee-note{left:568px;top:990px;width:262px;text-align:center;font-family:"M PLUS Rounded 1c",sans-serif;font-weight:800;font-size:21px;line-height:1.45;color:var(--rose-deep);text-shadow:0 0 4px #fff}
.footer{left:0;top:1090px;width:849px;height:110px;background:var(--white);border-top:3px solid var(--rose)}
.company{left:14px;top:1100px;width:340px}
.company .caption{font-size:10px;color:var(--ink)}
.company .name{display:flex;align-items:center;gap:8px;font-weight:900;font-size:26px;color:var(--wine);margin:2px 0}
.company .name i{display:inline-block;width:22px;height:22px;border-radius:50%;background:var(--rose)}
.company .fine{font-size:9px;line-height:1.4;color:var(--ink)}
.hours{left:600px;top:1096px;background:var(--wine);color:#fff;font-size:10px;padding:2px 8px;border-radius:3px}
.contact{left:360px;top:1118px;width:470px;text-align:right;color:var(--rose-deep)}
.contact .ask{font-size:14px;font-weight:700;color:var(--ink)}
.contact .tel{display:inline-flex;align-items:center;gap:8px;font-weight:900;font-size:42px;line-height:1}
.contact .url{font-size:13px;color:var(--ink);margin-top:4px}
</style>
</head>
<body>
<main class="flyer">
  <div class="rose-backdrop" role="img" aria-label="淡いピンクのバラの花を敷き詰めた背景装飾"></div>

  <h1 class="abs headline">テナント様募集中</h1>
  <p class="abs building-name">メゾン楓ビル <span class="num">31</span> 北浜Ⅲ</p>
  <p class="abs address">所在地：大阪市西成区玉出3丁目8-21</p>

  <div class="abs map-slot">地図</div>
  <div class="abs building-photo" role="img" aria-label="夜のビル外観の写真"></div>

  <p class="abs recruit-tag">オーナーママ募集</p>
  <p class="abs lead">憧れていたオーナーママになりませんか？<br>未経験のあなたもお店を始めるチャンスです！！</p>

  <p class="abs welcome-band">見るだけでも<span class="accent">大歓迎！</span>お気軽にお問合せください</p>

  <p class="abs support-note">店舗・仕入業者<br>資金・申請手続など<br>女性スタッフがお手伝いさせていただきます</p>

  <div class="abs room-photo photo-a" role="img" aria-label="カウンター席のある店内写真"></div>
  <dl class="abs spec spec-a">
    <div><dt>賃料</dt><dd>98,000円</dd></div>
    <div><dt>共益費</dt><dd>20,000円</dd></div>
    <div><dt>礼金</dt><dd>20,000円</dd></div>
    <div><dt>面積</dt><dd>30㎡</dd></div>
    <div><dt>席数</dt><dd>20席</dd></div>
  </dl>

  <dl class="abs spec spec-b">
    <div><dt>賃料</dt><dd>98,000円</dd></div>
    <div><dt>共益費</dt><dd>20,000円</dd></div>
    <div><dt>礼金</dt><dd>20,000円</dd></div>
    <div><dt>面積</dt><dd>30㎡</dd></div>
    <div><dt>席数</dt><dd>20席</dd></div>
  </dl>
  <div class="abs room-photo photo-b" role="img" aria-label="カウンター席のある店内写真"></div>

  <div class="abs room-photo photo-c" role="img" aria-label="カウンター席のある店内写真"></div>
  <dl class="abs spec spec-c">
    <div><dt>賃料</dt><dd>98,000円</dd></div>
    <div><dt>共益費</dt><dd>20,000円</dd></div>
    <div><dt>礼金</dt><dd>20,000円</dd></div>
    <div><dt>面積</dt><dd>30㎡</dd></div>
    <div><dt>席数</dt><dd>20席</dd></div>
  </dl>

  <p class="abs fee-note">仲介手数料不要<br>初期投資額を抑えた<br>開業・開店をサポート</p>

  <footer class="abs footer"></footer>
  <div class="abs company">
    <p class="caption">スナックビル・バー専門賃貸</p>
    <p class="name"><i></i>株式会社 楓</p>
    <p class="fine">大阪市西成区玉出3丁目8-21<br>宅建免許 大阪府知事(1)第00000号</p>
  </div>
  <p class="abs hours">営業時間 9:00〜18:00（日・祝を除く）</p>
  <div class="abs contact">
    <p class="ask">お電話でのお問い合わせは</p>
    <p class="tel">
      <svg width="34" height="34" viewBox="0 0 24 24" aria-hidden="true"><path fill="#d6195a" d="M6.6 10.8a15 15 0 0 0 6.6 6.6l2.2-2.2a1 1 0 0 1 1-.25 11.4 11.4 0 0 0 3.6.57 1 1 0 0 1 1 1V20a1 1 0 0 1-1 1A17 17 0 0 1 3 4a1 1 0 0 1 1-1h3.5a1 1 0 0 1 1 1c0 1.25.2 2.45.57 3.57a1 1 0 0 1-.25 1z"/></svg>
      0120-3-71928
    </p>
    <p class="url">http://kaede-hanamaru.co.jp/</p>
  </div>
</main>
</body>
</html>
```